Commercial Diving Company, Needs website designed and coded

We need a website designed for a new commercial diving company based on vancouver island. We fix docks using styrofoam billets installed underwater, as well as surveys, inspections, and plan to move into the aquaculture industry. Our main focus at the moment is flotation and want our customers to have an easy to navigate web page to answer their questions so they can understand a little more about what our service provides. We would like to see our main logo colours (blue/yellow) . The final design should communicate Safety, Success, and trustworthy work.

Target Market(s)

Fishing lodges, Fish Farms, Marinas, Logging Camps, Float home owners, Lake House owners

Coding

Coded - Design and coding required

Number of Pages Required

3 page

Font styles to use
Sans Serif

Colors
3277b5
fbed22
85cae6
ffffff
fbf289
00a990

Requirements
Must have
• Pages: about us, services offered, link to facebook, contact us - with link to email, phone

Book a free quote tab

```html
<!DOCTYPE html>
<html lang="en">
<head>
<meta charset="utf-8">
<title>Tideline Dive</title>
<link href="https://fonts.googleapis.com/css2?family=Poppins:wght@300;400;500;600;700;800&display=swap" rel="stylesheet">
<style>
:root{
  --blue:#1a6fdf;
  --blue-deep:#1557b3;
  --navy:#14233a;
  --yellow:#f4c434;
  --teal:#12a88b;
  --text:#2a2a2a;
  --white:#ffffff;
}
*{margin:0;padding:0;box-sizing:border-box}
html,body{width:1200px;height:3571px;overflow:hidden;background:var(--white)}
body{position:relative;font-family:'Poppins',sans-serif;color:var(--text)}
.abs{position:absolute}
a{color:inherit;text-decoration:none}

/* header */
.hero-photo{left:0;top:0;width:1200px;height:460px;background:linear-gradient(180deg,#a9d3f2 0%,#cfe6f5 30%,#6f8f7a 52%,#3f5d4e 68%,#2d5a7a 100%)}
.hero-cut{left:0;top:0}
.nav{top:48px;left:132px;display:flex;gap:44px;font-size:13px;color:#23344a}
.nav a{padding-bottom:6px}
.nav .active{color:var(--blue-deep);border-bottom:3px solid var(--blue-deep)}
.brand{top:46px;left:520px;width:160px;display:flex;align-items:center;justify-content:center;gap:8px;font-weight:700;font-size:22px;color:var(--blue-deep)}
.brand-dot{display:block;width:22px;height:22px;border-radius:50%;background:var(--yellow)}
.pill{top:42px;height:41px;border-radius:21px;color:var(--white);font-size:11.5px;font-weight:500;display:flex;align-items:center;justify-content:center;gap:7px;white-space:nowrap;box-shadow:0 4px 10px rgba(0,0,0,.15)}
.pill-email{left:692px;width:205px;background:var(--yellow)}
.pill-phone{left:911px;width:195px;background:var(--blue)}
.hero-title{left:92px;top:172px;font-size:26px;font-weight:600;color:var(--navy);white-space:nowrap}
.hero-sub{left:92px;top:208px;font-size:21px;font-weight:300;line-height:26px;color:var(--navy);width:240px}
.btn{display:flex;align-items:center;justify-content:center;color:var(--white);background:var(--blue);border-radius:22px;font-size:13px}
.hero-btn{left:92px;top:298px;width:212px;height:40px;font-size:14px}
.arrow{left:1064px;width:42px;height:42px;border-radius:50%;display:flex;align-items:center;justify-content:center}
.arrow-prev{top:174px;background:var(--yellow)}
.arrow-next{top:226px;border:2px solid var(--white);background:rgba(255,255,255,.15)}

/* banner areas */
.banner{display:flex;align-items:center;justify-content:center;background:var(--yellow);border-radius:10px;font-weight:300;font-size:44px;letter-spacing:1px}
.banner-top{left:65px;top:430px;width:1030px;height:120px;color:var(--white)}
.banner-foot{left:92px;top:2960px;width:1030px;height:120px;color:#1e2a3a}

/* welcome */
.welcome-title{left:94px;top:630px;font-size:30px;font-weight:700;color:var(--navy)}
.welcome-sub{left:93px;top:676px;width:560px;font-size:20px;line-height:26px;color:#333}
.welcome-text{left:93px;top:756px;width:590px;font-size:13px;line-height:25px;color:#333}
.btn-small{height:36px;width:133px;font-size:10.5px;border-radius:18px}
.welcome-btn{left:93px;top:898px}

.contact{left:741px;top:592px;width:364px;height:441px;background:var(--blue)}
.contact-title{position:absolute;left:24px;top:40px;color:var(--white);font-weight:700;font-size:19px}
.contact-panel{position:absolute;left:24px;top:73px;width:313px;height:323px;background:var(--white)}
.field{position:absolute;left:10px;width:292px;height:39px;border:2px solid var(--blue);background:var(--white);display:flex;align-items:flex-start}
.field .ico{width:40px;height:100%;background:var(--blue);display:flex;align-items:flex-start;justify-content:center;padding-top:8px}
.field span{font-size:12px;color:var(--blue);letter-spacing:1px;padding:9px 0 0 8px}
.field-area .ico{height:38px}
.submit{position:absolute;left:10px;top:269px;width:292px;height:40px;background:var(--blue);color:var(--white);font-weight:700;font-size:14px;display:flex;align-items:center;justify-content:center}

/* what we do */
.ring{left:405px;top:1244px;width:270px;height:270px;border-radius:50%;border:46px solid var(--yellow)}
.photo-a{left:93px;top:1152px;width:309px;height:325px;background:linear-gradient(160deg,#5f8fb8,#5a6f5a 55%,#8aa0b0)}
.photo-b{left:251px;top:1325px;width:305px;height:323px;background:linear-gradient(180deg,#7fb0e0,#3e6046 45%,#b7b9b4 70%,#4e4a3c)}
.hatch{left:716px;top:1115px;width:67px;height:28px;background:repeating-linear-gradient(45deg,#e4e4e4 0 2px,#f6f6f6 2px 5px)}
.wwd-title{left:715px;top:1132px;font-size:32px;font-weight:800;color:var(--navy)}
.wwd-sub{left:716px;top:1174px;width:400px;font-size:22px;line-height:27px;color:var(--navy);letter-spacing:.5px}
.wwd-text{left:718px;top:1244px;width:370px;font-size:13.5px;line-height:20px;color:#333}
.check{left:748px;width:24px;height:24px;border-radius:50%;background:#4a86d8;display:flex;align-items:center;justify-content:center}
.item-title{font-size:15px;font-weight:600;color:var(--navy)}
.item-text{font-size:12px;line-height:19px;width:305px;color:#333;letter-spacing:.3px}
.wwd-btn{left:786px;top:1606px}

/* services */
.services{left:0;top:1832px;width:1200px;height:1260px;background:linear-gradient(180deg,#2d3849 0%,#27313f 60%,#233044 100%)}
.svc-title{left:0;top:1876px;width:1200px;text-align:center;color:var(--white);font-size:34px;font-weight:800}
.svc-tag{left:0;top:1924px;width:1200px;text-align:center;color:var(--yellow);font-size:12.5px;letter-spacing:4px}
.card{width:319px;text-align:center}
.card-img{height:182px;background:linear-gradient(170deg,#6f9a6f,#8b6b4d 50%,#4f6a86)}
.card-title{margin-top:32px;color:var(--yellow);font-weight:600;font-size:16px;letter-spacing:.5px}
.card-text{margin:12px auto 0;width:245px;color:#c9ced6;font-size:13px;line-height:18px;letter-spacing:.5px}
.card-btn{margin:24px auto 0;width:141px;height:37px;background:var(--teal);border:1px solid #2fd0b0;color:var(--white);font-size:11.5px;letter-spacing:1.5px;display:flex;align-items:center;justify-content:center;gap:8px}

/* footer */
.footer-bg{left:0;top:2930px}
.f-head{font-size:11.5px;font-weight:600;color:var(--white);padding-top:8px;position:absolute}
.f-head::before{content:"";position:absolute;left:0;top:0;width:24px;height:3px;background:var(--yellow)}
.f-text{font-size:12.5px;line-height:20px;color:var(--white)}
.f-list{list-style:none;font-size:12.5px;color:var(--white)}
.f-list li{height:27px;display:flex;align-items:center;gap:8px}
.social{display:flex;gap:10px}
.social i{display:block;width:16px;height:16px;border-radius:50%;border:2px solid var(--yellow)}
.f-label{color:var(--yellow);font-weight:600}
.footer-brand{left:500px;top:3400px;width:200px;display:flex;justify-content:center;align-items:center;gap:8px;font-weight:700;font-size:22px;color:var(--white)}
.copy{left:0;top:3492px;width:1200px;text-align:center;color:var(--white);font-size:13.5px}
.copy b{color:var(--yellow)}
</style>
</head>
<body>

<!-- hero -->
<div class="abs hero-photo" role="img" aria-label="Floating dock house on a calm lake with forested hills behind"></div>
<svg class="abs hero-cut" width="1200" height="580" viewBox="0 0 1200 580">
  <path d="M0 380 Q300 470 600 500 Q900 490 1200 410 L1200 580 L0 580 Z" fill="#fff"/>
</svg>
<div class="abs banner banner-top" role="img" aria-label="Yellow ribbon banner reading Dive Services">DIVE SERVICES</div>

<nav class="abs nav"><a class="active" href="#">HOME</a><a href="#">ABOUT US</a><a href="#">SERVICES</a></nav>
<div class="abs brand"><i class="brand-dot"></i>Tideline</div>
<a class="abs pill pill-email" href="#"><svg width="16" height="14" viewBox="0 0 16 14"><rect x="1" y="2" width="14" height="11" fill="none" stroke="#fff" stroke-width="1.5"/><path d="M1 3l7 5 7-5" fill="none" stroke="#fff" stroke-width="1.5"/></svg>Email : hi@tidelinedive.com</a>
<a class="abs pill pill-phone" href="#"><svg width="16" height="16" viewBox="0 0 16 16"><path d="M3 1l3 3-2 2q2 4 6 6l2-2 3 3-2 2Q6 14 1 3z" fill="none" stroke="#fff" stroke-width="1.3"/></svg>Phone : 1800 555 01472</a>

<h1 class="abs hero-title">ALL THE FUN STARTS HERE</h1>
<p class="abs hero-sub">Unknown printer took galley of type and scrambled it</p>
<a class="abs btn hero-btn" href="#">Get in Touch</a>
<div class="abs arrow arrow-prev"><svg width="12" height="16"><path d="M9 2L3 8l6 6" fill="none" stroke="#fff" stroke-width="1.5"/></svg></div>
<div class="abs arrow arrow-next"><svg width="12" height="16"><path d="M3 2l6 6-6 6" fill="none" stroke="#fff" stroke-width="1.5"/></svg></div>

<!-- welcome -->
<h2 class="abs welcome-title">WELCOME</h2>
<p class="abs welcome-sub">Simply dummy text of the printing and typesetting industry. Lorem Ipsum has been the.</p>
<p class="abs welcome-text">Lorem Ipsum is simply dummy text of the printing and typesetting industry. Lorem Ipsum has been the industry's standard dummy text ever since the 1500s, when an unknown printer took a galley of type and scrambled it to make a type specimen book. It has survived not only five centuries, but also the leap into electronic typesetting, remaining essentially unchanged.</p>
<a class="abs btn btn-small welcome-btn" href="#">READ MORE</a>

<form class="abs contact">
  <h3 class="contact-title">CONTACT US FORM</h3>
  <div class="contact-panel">
    <div class="field" style="top:9px"><div class="ico"><svg width="18" height="18"><circle cx="9" cy="5" r="4" fill="#fff"/><path d="M1 18q8-12 16 0z" fill="#fff"/></svg></div><span>Name:</span></div>
    <div class="field" style="top:58px"><div class="ico"><svg width="20" height="16"><rect x="1" y="2" width="18" height="12" fill="none" stroke="#fff" stroke-width="1.5"/><path d="M1 3l9 6 9-6" fill="none" stroke="#fff" stroke-width="1.5"/></svg></div><span>Email:</span></div>
    <div class="field" style="top:107px"><div class="ico"><svg width="20" height="18"><path d="M3 1l4 4-2 2q3 5 7 7l2-2 4 4-2 2Q6 16 1 4z" fill="none" stroke="#fff" stroke-width="1.4"/></svg></div><span>Phone:</span></div>
    <div class="field field-area" style="top:160px;height:93px"><div class="ico"><svg width="22" height="20"><rect x="1" y="1" width="20" height="13" rx="2" fill="#fff"/><path d="M5 14v5l5-5z" fill="#fff"/><circle cx="7" cy="7.5" r="1.3" fill="#1a6fdf"/><circle cx="11" cy="7.5" r="1.3" fill="#1a6fdf"/><circle cx="15" cy="7.5" r="1.3" fill="#1a6fdf"/></svg></div><span>Comments:</span></div>
    <div class="submit">SUBMIT NOW</div>
  </div>
</form>

<!-- what we do -->
<div class="abs ring"></div>
<div class="abs photo-a" role="img" aria-label="Dive crew in life jackets aboard a boat beside a dock"></div>
<div class="abs photo-b" role="img" aria-label="Float houses resting on a dock with flotation billets"></div>
<div class="abs hatch"></div>
<h2 class="abs wwd-title">WHAT WE DO</h2>
<p class="abs wwd-sub">Specimen book. It has survived not only five centuries.</p>
<p class="abs wwd-text">Type specimen book. It has survived not only five centuries, but also the leap into electronic typesetting, remaining essentially unchanged.</p>

<div class="abs check" style="top:1362px"><svg width="12" height="10"><path d="M1 5l3.5 3.5L11 1" fill="none" stroke="#fff" stroke-width="2"/></svg></div>
<div class="abs" style="left:785px;top:1362px">
  <div class="item-title">Sample text goes here</div>
  <p class="item-text" style="margin-top:8px">We are privileged to work with hundred future-thinking awesome businesses including many of the world's top hardware</p>
</div>
<div class="abs check" style="top:1485px"><svg width="12" height="10"><path d="M1 5l3.5 3.5L11 1" fill="none" stroke="#fff" stroke-width="2"/></svg></div>
<div class="abs" style="left:788px;top:1485px">
  <div class="item-title">Sample text goes here</div>
  <p class="item-text" style="margin-top:8px">We are privileged to work with hundred future-thinking awesome businesses including many of the world's top hardware</p>
</div>
<a class="abs btn btn-small wwd-btn" href="#">READ MORE</a>

<!-- services -->
<section class="abs services"></section>
<h2 class="abs svc-title">SERVICES</h2>
<p class="abs svc-tag">PROVIDE EXCLUSIVE SERVICES</p>

<div class="abs card" style="left:93px;top:1975px"><div class="card-img" role="img" aria-label="Wooden cabin on a floating dock"></div><div class="card-title">Marketing Strategy</div><p class="card-text">We are privileged to work with hundred future-thinking awesome businesses including many of the world's top hardware</p><div class="card-btn">READ MORE <svg width="18" height="16"><path d="M2 2l14 12M16 2L2 14" stroke="#fff" stroke-width="2"/></svg></div></div>
<div class="abs card" style="left:442px;top:1975px"><div class="card-img" role="img" aria-label="Metal pontoon frame being prepared on shore" style="background:linear-gradient(170deg,#8fa3a0,#b9bdbd 50%,#7a6f5c)"></div><div class="card-title">Marketing Strategy</div><p class="card-text">We are privileged to work with hundred future-thinking awesome businesses including many of the world's top hardware</p><div class="card-btn">READ MORE <svg width="18" height="16"><path d="M2 2l14 12M16 2L2 14" stroke="#fff" stroke-width="2"/></svg></div></div>
<div class="abs card" style="left:790px;top:1975px"><div class="card-img" role="img" aria-label="Divers working from a boat on the water" style="background:linear-gradient(170deg,#4f86b8,#8a9aa6 50%,#3e5a78)"></div><div class="card-title">Marketing Strategy</div><p class="card-text">We are privileged to work with hundred future-thinking awesome businesses including many of the world's top hardware</p><div class="card-btn">READ MORE <svg width="18" height="16"><path d="M2 2l14 12M16 2L2 14" stroke="#fff" stroke-width="2"/></svg></div></div>

<div class="abs card" style="left:93px;top:2387px"><div class="card-img" role="img" aria-label="White float homes along a forested shoreline" style="background:linear-gradient(170deg,#6f9fd6,#6d8a5e 45%,#d8d8d2 70%,#5d5242)"></div><div class="card-title">Marketing Strategy</div><p class="card-text">We are privileged to work with hundred future-thinking awesome businesses including many of the world's top hardware</p><div class="card-btn">READ MORE <svg width="18" height="16"><path d="M2 2l14 12M16 2L2 14" stroke="#fff" stroke-width="2"/></svg></div></div>
<div class="abs card" style="left:442px;top:2387px"><div class="card-img" role="img" aria-label="Float houses moored on a lake" style="background:linear-gradient(170deg,#7fb2e6,#4d6b48 45%,#e2e2de 70%,#4b5e6e)"></div><div class="card-title">Marketing Strategy</div><p class="card-text">We are privileged to work with hundred future-thinking awesome businesses including many of the world's top hardware</p><div class="card-btn">READ MORE <svg width="18" height="16"><path d="M2 2l14 12M16 2L2 14" stroke="#fff" stroke-width="2"/></svg></div></div>
<div class="abs card" style="left:790px;top:2387px"><div class="card-img" role="img" aria-label="Submerged dock section beside a walkway" style="background:linear-gradient(170deg,#6f7f86,#4c5c62 50%,#9aa2a2)"></div><div class="card-title">Marketing Strategy</div><p class="card-text">We are privileged to work with hundred future-thinking awesome businesses including many of the world's top hardware</p><div class="card-btn">READ MORE <svg width="18" height="16"><path d="M2 2l14 12M16 2L2 14" stroke="#fff" stroke-width="2"/></svg></div></div>

<!-- footer -->
<svg class="abs footer-bg" width="1200" height="641" viewBox="0 0 1200 641">
  <defs><linearGradient id="fg" x1="0" y1="0" x2="0" y2="1"><stop offset="0" stop-color="#1a5fbf"/><stop offset="1" stop-color="#1450a8"/></linearGradient></defs>
  <path d="M0 170 Q600 -10 1200 170 L1200 641 L0 641 Z" fill="url(#fg)"/>
</svg>
<div class="abs banner banner-foot" role="img" aria-label="Yellow ribbon banner reading Dive Services">DIVE SERVICES</div>

<div class="f-head" style="left:94px;top:3138px">SITEMAP</div>
<p class="abs f-text" style="left:94px;top:3172px;width:250px">Condimentum rhoncus, sem quam semper libero, sit amet adipiscing sem neque sed ipsum. Nam quam nunc, blandit vel, luctus.</p>
<div class="abs f-text" style="left:94px;top:3268px;font-weight:600;font-size:12px">Follow Us</div>
<div class="abs social" style="left:94px;top:3292px" aria-label="Social links"><i></i><i></i><i></i><i></i></div>

<div class="f-head" style="left:417px;top:3138px">SITEMAP</div>
<ul class="abs f-list" style="left:417px;top:3166px">
  <li><svg width="12" height="10"><path d="M1 5l3.5 3.5L11 1" fill="none" stroke="#f4c434" stroke-width="2"/></svg>Home</li>
  <li><svg width="12" height="10"><path d="M1 5l3.5 3.5L11 1" fill="none" stroke="#f4c434" stroke-width="2"/></svg>About us</li>
  <li><svg width="12" height="10"><path d="M1 5l3.5 3.5L11 1" fill="none" stroke="#f4c434" stroke-width="2"/></svg>Services</li>
  <li><svg width="12" height="10"><path d="M1 5l3.5 3.5L11 1" fill="none" stroke="#f4c434" stroke-width="2"/></svg>Contact US</li>
</ul>

<div class="f-head" style="left:625px;top:3138px">OUR SERVICES</div>
<ul class="abs f-list" style="left:625px;top:3166px">
  <li><svg width="12" height="10"><path d="M1 5l3.5 3.5L11 1" fill="none" stroke="#f4c434" stroke-width="2"/></svg>Condimentum</li>
  <li><svg width="12" height="10"><path d="M1 5l3.5 3.5L11 1" fill="none" stroke="#f4c434" stroke-width="2"/></svg>rhoncus, sem quam</li>
  <li><svg width="12" height="10"><path d="M1 5l3.5 3.5L11 1" fill="none" stroke="#f4c434" stroke-width="2"/></svg>semper libero, sit</li>
  <li><svg width="12" height="10"><path d="M1 5l3.5 3.5L11 1" fill="none" stroke="#f4c434" stroke-width="2"/></svg>amet adipiscing</li>
  <li><svg width="12" height="10"><path d="M1 5l3.5 3.5L11 1" fill="none" stroke="#f4c434" stroke-width="2"/></svg>sem neque sed</li>
  <li><svg width="12" height="10"><path d="M1 5l3.5 3.5L11 1" fill="none" stroke="#f4c434" stroke-width="2"/></svg>ipsum. Nam quam</li>
</ul>

<div class="f-head" style="left:883px;top:3138px">COMPANY ADDRESS</div>
<p class="abs f-text" style="left:885px;top:3172px;width:230px;font-size:12px;line-height:16px">Porem awesome dolor sitework amet, consetur acing elit, sed do eiusmod ligal</p>
<p class="abs f-text" style="left:885px;top:3232px;width:230px;font-size:12px;line-height:16px"><span class="f-label">Address:</span> 18 Harbour Lane, Comox Bay, Canada</p>
<p class="abs f-text" style="left:885px;top:3278px;font-size:12px"><span class="f-label">Phone:</span> 25055501938</p>
<p class="abs f-text" style="left:885px;top:3310px;font-size:12px"><span class="f-label">Email:</span> info@tidelinedive.com</p>

<div class="abs footer-brand"><i class="brand-dot"></i>Tideline</div>
<p class="abs copy">Copyright © 2020 <b>Tideline</b></p>

</body>
</html>
```